Lodging Refresh Partners - Tabletop Display

We need a 5'x5' trade show display for a hotel renovation company named "Lodging Refresh Partners." Lodging Refresh Partners is the most complete authority on hotel renovation in the country, and we're the only 100% turn-key renovator in Colorado. With one phone call, we deliver an approved design, FF&E purchasing, logistics, construction, installation, and warranty administration. The design needs to convey professionalism. Our goal is to help our clients reduce costs and reduce stress while achieving the best results. The colors should align with the attached brochure for our Raleigh office.

Target Market(s)

Hotel owners and general managers

Industry/Entity Type

Design Agency

Colors
3277b5
85acd3
cfdeed

Requirements
Must have
• Our product is a blend of design and construction. I need to convey our services and attention to detail without seeming salesy, bold, or aggressive. The goal is to convey confidence and help to relax our potential client base.
Nice to have
• Possibly one or more photos of completed projects. Not sure if exterior, lobby, or guest room photos would be best. I can send files via dropbox if that's helpful.
Should not have
• I've included a photo of the old display at a trade show. I strongly dislike the yellow and red on the display. Please try to stick to the color palette of the attached brochure.

```html
<!DOCTYPE html>
<html lang="en">
<head>
<meta charset="utf-8">
<title>Lodging Refresh Partners – Tabletop Display</title>
<link rel="stylesheet" href="https://fonts.googleapis.com/css2?family=Roboto:wght@300;400;700&display=swap">
<style>
  :root {
    --brand-blue: #3567b3;
    --brand-blue-mid: #85acd3;
    --brand-blue-pale: #cfdeed;
    --paper: #ffffff;
    --stage: #141414;
    --patio-warm: #b89a7a;
    --patio-stone: #8f7f70;
    --dusk-wall: #d8cbb6;
    --room-red: #8a3a2c;
    --room-cream: #e3d8c6;
    --sky: #9bb5d6;
  }
  html, body {
    margin: 0;
    width: 1200px;
    height: 1200px;
    overflow: hidden;
    background: var(--stage);
    font-family: "Roboto", Arial, sans-serif;
  }
  .board {
    position: absolute;
    top: 226px;
    width: 538px;
    height: 536px;
    background: var(--paper);
  }
  .board--services { left: 30px; }
  .board--headline { left: 635px; }
  .board svg { display: block; width: 538px; height: 536px; }
  .brand-name { font-family: "Roboto", Arial, sans-serif; font-weight: 700; fill: var(--brand-blue); }
  .band-label { font-family: "Roboto", Arial, sans-serif; font-weight: 700; font-size: 14px; fill: var(--paper); }
  .footer-line { font-family: "Roboto", Arial, sans-serif; font-weight: 400; font-size: 14px; fill: var(--brand-blue); }
  .service-item { font-family: "Roboto", Arial, sans-serif; font-weight: 400; font-size: 15.5px; fill: var(--brand-blue); }
  .headline { font-family: "Roboto", Arial, sans-serif; font-weight: 300; font-size: 33px; fill: var(--paper); }
  .headline-strong { font-weight: 700; }
  .contact-line { font-family: "Roboto", Arial, sans-serif; font-weight: 300; font-size: 17.5px; fill: var(--paper); }
  .web-line { font-family: "Roboto", Arial, sans-serif; font-weight: 300; font-size: 14.5px; fill: var(--paper); }
</style>
</head>
<body>

<section class="board board--services">
  <svg viewBox="0 0 538 536" xmlns="http://www.w3.org/2000/svg">
    <defs>
      <linearGradient id="patioGlow" x1="0" y1="0" x2="0" y2="1">
        <stop offset="0" stop-color="#d9cdb9"/>
        <stop offset="0.45" stop-color="#a88c6e"/>
        <stop offset="1" stop-color="#8d8479"/>
      </linearGradient>
      <linearGradient id="roomTone" x1="0" y1="0" x2="1" y2="1">
        <stop offset="0" stop-color="#efe9e0"/>
        <stop offset="1" stop-color="#9c9087"/>
      </linearGradient>
      <linearGradient id="lobbyTone" x1="0" y1="0" x2="1" y2="1">
        <stop offset="0" stop-color="#c9a57c"/>
        <stop offset="1" stop-color="#6f5a48"/>
      </linearGradient>
      <linearGradient id="diningTone" x1="0" y1="0" x2="1" y2="1">
        <stop offset="0" stop-color="#b7884f"/>
        <stop offset="1" stop-color="#8a3a2c"/>
      </linearGradient>
      <linearGradient id="exteriorTone" x1="0" y1="0" x2="0" y2="1">
        <stop offset="0" stop-color="#9bb5d6"/>
        <stop offset="1" stop-color="#c9ae86"/>
      </linearGradient>
    </defs>

    <rect x="0" y="13" width="538" height="441" fill="url(#patioGlow)" role="img" aria-label="Photo of a hotel courtyard at dusk with a stone fire pit and patio seating"/>

    <rect x="36" y="13" width="130" height="107" fill="var(--paper)"/>
    <rect x="52" y="36" width="12" height="12" fill="var(--brand-blue)"/>
    <text class="brand-name" font-size="15" x="52" y="70">Lodging</text>
    <text class="brand-name" font-size="15" x="52" y="88">Refresh</text>
    <text class="brand-name" font-size="15" x="52" y="106">Partners</text>

    <g class="service-bands">
      <rect x="367" y="193" width="171" height="52" fill="var(--brand-blue)"/>
      <circle cx="367" cy="217" r="42" fill="url(#roomTone)" stroke="var(--paper)" stroke-width="2" role="img" aria-label="Photo of a renovated guest room"/>
      <text class="band-label" x="425" y="215">Design</text>
      <text class="band-label" x="425" y="232">Specification</text>

      <rect x="302" y="270" width="236" height="52" fill="var(--brand-blue)"/>
      <circle cx="302" cy="296" r="42" fill="url(#lobbyTone)" stroke="var(--paper)" stroke-width="2" role="img" aria-label="Photo of a lobby with a stone fireplace"/>
      <text class="band-label" x="356" y="293">FF&amp;E</text>
      <text class="band-label" x="356" y="310">Logistics</text>

      <rect x="238" y="349" width="300" height="52" fill="var(--brand-blue)"/>
      <circle cx="238" cy="374" r="42" fill="url(#diningTone)" stroke="var(--paper)" stroke-width="2" role="img" aria-label="Photo of a hotel dining area with red chairs"/>
      <text class="band-label" x="294" y="372">Construction</text>
      <text class="band-label" x="294" y="389">Installation</text>

      <rect x="174" y="429" width="364" height="51" fill="var(--brand-blue)"/>
      <circle cx="174" cy="454" r="42" fill="url(#exteriorTone)" stroke="var(--paper)" stroke-width="2" role="img" aria-label="Photo of a hotel building exterior"/>
      <text class="band-label" x="231" y="460">Warranty Administration</text>
    </g>

    <text class="footer-line" x="26" y="522">www.lodgingrefresh.com</text>
    <text class="footer-line" x="510" y="522" text-anchor="end">For Assistance - Dial Now: 303-555-0148</text>
  </svg>
</section>

<section class="board board--headline">
  <svg viewBox="0 0 538 536" xmlns="http://www.w3.org/2000/svg">
    <defs>
      <linearGradient id="exteriorStrip" x1="0" y1="0" x2="0" y2="1">
        <stop offset="0" stop-color="#8fb0d8"/>
        <stop offset="1" stop-color="#c8ad88"/>
      </linearGradient>
      <linearGradient id="diningStrip" x1="0" y1="0" x2="1" y2="1">
        <stop offset="0" stop-color="#6e4a34"/>
        <stop offset="1" stop-color="#9c3a2e"/>
      </linearGradient>
      <linearGradient id="lobbyStrip" x1="0" y1="0" x2="1" y2="1">
        <stop offset="0" stop-color="#d9b98f"/>
        <stop offset="1" stop-color="#a58a6c"/>
      </linearGradient>
      <linearGradient id="roomStrip" x1="0" y1="0" x2="1" y2="1">
        <stop offset="0" stop-color="#e8e6e2"/>
        <stop offset="1" stop-color="#6d6d70"/>
      </linearGradient>
      <linearGradient id="patioPhoto" x1="0" y1="0" x2="0" y2="1">
        <stop offset="0" stop-color="#d5c8b3"/>
        <stop offset="0.5" stop-color="#a3876a"/>
        <stop offset="1" stop-color="#9a9189"/>
      </linearGradient>
    </defs>

    <g class="photo-strip">
      <polygon points="0,0 169,0 133,110 0,110" fill="url(#exteriorStrip)" role="img" aria-label="Photo of a hotel building exterior"/>
      <polygon points="177,0 313,0 277,110 141,110" fill="url(#diningStrip)" role="img" aria-label="Photo of a hotel dining room"/>
      <polygon points="321,0 461,0 425,110 285,110" fill="url(#lobbyStrip)" role="img" aria-label="Photo of a hotel lounge with fireplace"/>
      <polygon points="469,0 538,0 538,110 433,110" fill="url(#roomStrip)" role="img" aria-label="Photo of a modern guest room"/>
    </g>

    <rect x="37" y="132" width="12" height="12" fill="var(--brand-blue)"/>
    <text class="brand-name" font-size="16" x="37" y="166">Lodging</text>
    <text class="brand-name" font-size="16" x="37" y="185">Refresh</text>
    <text class="brand-name" font-size="16" x="37" y="204">Partners</text>

    <g class="service-list">
      <text class="service-item" x="253" y="139">›&#160; Design</text>
      <text class="service-item" x="253" y="158">›&#160; Specification</text>
      <text class="service-item" x="253" y="176">›&#160; FF&amp;E</text>
      <text class="service-item" x="253" y="195">›&#160; Logistics</text>
      <text class="service-item" x="394" y="139">›&#160; Construction</text>
      <text class="service-item" x="394" y="158">›&#160; Installation</text>
      <text class="service-item" x="394" y="176">›&#160; Warranty -</text>
      <text class="service-item" x="407" y="195">Administration</text>
    </g>

    <rect x="0" y="210" width="538" height="326" fill="url(#patioPhoto)" role="img" aria-label="Photo of a hotel courtyard with a lit stone fire pit"/>
    <polygon points="301,210 538,210 538,536 154,536" fill="var(--paper)"/>
    <polygon points="317,210 538,210 538,536 167,536" fill="var(--brand-blue)"/>

    <text class="headline" x="309" y="277">A COMPLETE</text>
    <text class="headline" x="309" y="315">RENOVATION</text>
    <text class="headline" x="309" y="353">WITH JUST</text>
    <text class="headline headline-strong" x="309" y="391">ONE CALL!</text>

    <text class="contact-line" x="309" y="448">For Assistance...</text>
    <text class="contact-line" x="309" y="470">Dial Now: 303-555-0148</text>

    <text class="web-line" x="309" y="523">www.lodgingrefresh.com</text>
  </svg>
</section>

</body>
</html>
```